Wedding Startup Full Website Design

We've just completed our online platform and need to create a website that represents our brand and vision, and clearly communicates our features and value proposition to potential users. There are a minimum of 4 pages that need to be designed. One geared toward wedding professionals (venues/vendors/coordinators), another toward engaged couples, one showcasing features, and an 'About Us' page.

The designer will creative freedom to create a unique UI/UX as long as it represents our brand and is relevant to our target audience/market. The ideal candidate will be able to assume the mindset of someone working in the wedding industry and/or an engaged couple. Ability to create illustrations is a plus.

Copy will be provided as needed. We will reimburse for stock images (pending approval before purchasing), but sourcing the stock images will be the responsibility of the designer.

Our current website: https://www.trelmora.com
Updates

Our project has now been guaranteed! We look forward to finding the perfect design for our site pages!

Still waiting for a design that stands out from the rest and aligns with the creative brief.

Target Market(s)

Wedding Professionals and Engaged Couples

Industry/Entity Type

Wedding

Number of Pages Required

4 page

Font styles to use
Sans Serif

Colors
ffffff
fbd4d5
f59195
33a6d7
cadf82
86cfc6

Requirements
Must have
• Common sense stuff like having a unified brand that accurately represents our platform, speaks to our target market, and clearly articulates our vision
Nice to have
• Illustrations
Should not have
• Overly cheesy or childish. We want to be professional but still embrace the wedding culture.

```html
<!DOCTYPE html>
<html lang="en">
<head>
<meta charset="utf-8">
<title>Trelmora — Wedding Planning Platform</title>
<link rel="stylesheet" href="https://fonts.googleapis.com/css2?family=Courgette&family=Open+Sans:wght@300;400;600&display=swap">
<style>
  :root {
    --white: #ffffff;
    --blush: #fbd4d5;
    --coral: #f59195;
    --sky: #33a6d7;
    --lime: #b9d12b;
    --teal: #86cfc6;
    --ink: #3d3d3d;
    --muted: #c4c4c4;
    --script: "Courgette", cursive;
    --sans: "Open Sans", sans-serif;
  }
  * { margin: 0; padding: 0; box-sizing: border-box; }
  html, body { width: 960px; height: 1200px; overflow: hidden; }
  body { position: relative; background: var(--white); font-family: var(--sans); color: var(--ink); }

  .topbar { position: absolute; top: 0; left: 0; width: 960px; height: 32px; background: var(--coral); color: var(--white); font-size: 11px; }
  .contact-item { position: absolute; top: 0; height: 32px; display: flex; align-items: center; gap: 7px; }
  .contact-item.email { left: 24px; }
  .contact-item.phone { left: 158px; }
  .social-list { position: absolute; right: 12px; top: 6px; display: flex; gap: 5px; }
  .social-slot { width: 20px; height: 20px; border: 1px solid var(--white); border-radius: 4px; display: flex; align-items: center; justify-content: center; }

  .site-header { position: absolute; top: 32px; left: 0; width: 960px; height: 95px; }
  .brand { position: absolute; left: 22px; top: 30px; display: flex; align-items: center; gap: 8px; font-family: var(--sans); font-weight: 400; font-size: 30px; color: var(--sky); letter-spacing: -0.5px; }
  .brand-mark { width: 14px; height: 14px; background: var(--coral); }
  .main-nav a { position: absolute; top: 38px; font-family: var(--script); font-size: 15.5px; color: var(--lime); text-decoration: none; white-space: nowrap; }

  .hero { position: absolute; top: 127px; left: 0; width: 960px; height: 411px; }
  .hero-photo { position: absolute; inset: 0; background: linear-gradient(100deg, #c9b8ac 0%, #b89a86 30%, #a7988e 55%, #5a5452 78%, #2f2d2d 100%); }
  .hero-title { position: absolute; top: 172px; left: 0; width: 960px; text-align: center; font-family: var(--script); font-weight: 400; font-size: 46px; line-height: 54px; color: var(--white); }
  .btn { position: absolute; display: flex; align-items: center; justify-content: center; font-family: var(--sans); font-size: 14.5px; text-decoration: none; }
  .btn-light { left: 414px; top: 300px; width: 133px; height: 37px; border: 1px solid var(--white); color: var(--white); }

  .section-title { position: absolute; left: 0; width: 960px; text-align: center; font-family: var(--script); font-weight: 400; color: var(--ink); }
  .steps-title { top: 566px; font-size: 35px; }

  .step { position: absolute; left: 83px; width: 420px; }
  .step-number { position: absolute; left: 0; top: 0; width: 64px; height: 64px; border-radius: 50%; background: var(--blush); color: var(--white); font-size: 22px; font-weight: 300; display: flex; align-items: center; justify-content: center; }
  .step-name { position: absolute; left: 88px; top: 0; font-size: 19px; font-weight: 400; color: var(--muted); }
  .step-text { position: absolute; left: 88px; top: 29px; width: 330px; font-size: 11px; font-weight: 300; line-height: 14px; color: var(--muted); }
  .step.is-active .step-number { background: var(--coral); }
  .step.is-active .step-name { color: #1f1f1f; }
  .step.is-active .step-text { color: #2a2a2a; font-weight: 400; }
  .step-1 { top: 681px; }
  .step-2 { top: 777px; }
  .step-3 { top: 873px; }
  .step-1 .step-number, .step-3 .step-number { opacity: 0.75; }

  .product-shot { position: absolute; left: 568px; top: 648px; width: 324px; height: 360px; background: linear-gradient(160deg, #eef3f3 0%, #d9dede 55%, #c9cccc 100%); border-radius: 6px; }

  .cta { position: absolute; top: 1036px; left: 0; width: 960px; height: 164px; background: var(--teal); }
  .cta-title { top: 18px; font-size: 34px; }
  .cta-text { position: absolute; top: 68px; left: 0; width: 960px; text-align: center; font-size: 14px; line-height: 17px; color: #222; }
  .btn-dark { left: 424px; top: 126px; width: 133px; height: 40px; border: 1px solid #333; color: #222; }
</style>
</head>
<body>
  <div class="topbar">
    <span class="contact-item email">
      <svg width="16" height="12" viewBox="0 0 16 12"><rect x="0.5" y="0.5" width="15" height="11" fill="none" stroke="#fff"/><path d="M0.5 0.5 L8 7 L15.5 0.5" fill="none" stroke="#fff"/></svg>
      info@trelmora.com
    </span>
    <span class="contact-item phone">
      <svg width="18" height="13" viewBox="0 0 18 13"><path d="M1 4 Q9 -1 17 4 L15 6 L12 5 L12 3.5 Q9 2.5 6 3.5 L6 5 L3 6 Z" fill="#fff"/><rect x="4" y="7" width="10" height="6" rx="1" fill="#fff"/></svg>
      +92 500 731 204 86
    </span>
    <div class="social-list">
      <span class="social-slot"></span>
      <span class="social-slot"></span>
      <span class="social-slot"></span>
      <span class="social-slot"></span>
      <span class="social-slot"></span>
      <span class="social-slot"></span>
      <span class="social-slot">
        <svg width="11" height="11" viewBox="0 0 11 11"><circle cx="4.5" cy="4.5" r="3.5" fill="none" stroke="#fff" stroke-width="1.5"/><path d="M7 7 L10.5 10.5" stroke="#fff" stroke-width="1.6"/></svg>
      </span>
    </div>
  </div>

  <header class="site-header">
    <div class="brand"><span class="brand-mark"></span>Trelmora</div>
    <nav class="main-nav">
      <a href="#" style="left:280px">Home</a>
      <a href="#" style="left:337px">About Us</a>
      <a href="#" style="left:424px">Features</a>
      <a href="#" style="left:510px">For Couples</a>
      <a href="#" style="left:625px">For Wedding Professionals</a>
      <a href="#" style="left:827px">Demo</a>
      <a href="#" style="left:885px">Contact</a>
    </nav>
  </header>

  <section class="hero">
    <div class="hero-photo" role="img" aria-label="Photo of a bride with a floral crown and a groom in a dark suit leaning close together"></div>
    <h1 class="hero-title">we’ll make your wedding<br>perfect</h1>
    <a class="btn btn-light" href="#">Get Started</a>
  </section>

  <h2 class="section-title steps-title">How to get started</h2>

  <div class="step step-1">
    <div class="step-number">1</div>
    <h3 class="step-name">Sign Up</h3>
    <p class="step-text">Create a free account on Trelmora to access popular collaboration tools. Get Started</p>
  </div>
  <div class="step step-2 is-active">
    <div class="step-number">2</div>
    <h3 class="step-name">Collborte</h3>
    <p class="step-text">Add clients within the application to better organize and manage event details.</p>
  </div>
  <div class="step step-3">
    <div class="step-number">3</div>
    <h3 class="step-name">Connect</h3>
    <p class="step-text">Linking your bank account within Trelmora to allow for seamless payments and monitoring.</p>
  </div>

  <div class="product-shot" role="img" aria-label="Desktop computer showing the Trelmora dashboard with balances and recent transactions"></div>

  <section class="cta">
    <h2 class="section-title cta-title">Get Started Today</h2>
    <p class="cta-text">We recently launched a demo version of Trelmora to allow users to see and interact with our platform.<br>Create a free account and see how Trelmora is changing the wedding planning process!</p>
    <a class="btn btn-dark" href="#">Access Demo</a>
  </section>
</body>
</html>
```